Corvalen Technologies Support Business Card

I would like a business card that doesn't focus on an individual role within our company but rather and call to action for current and potential clients to engage with us. We are a small business hybrid IT support company out of Metro Detroit in Michigan. Something that contains a QR code as an easy way to seek support. It should include and simple call to action but also refers to our company values. "Experience is Everything" "Obsessed with Impossible" and "Consistency Over Time Equals Trust". Our brand colors are typically a deeper/darker read, black, charcoal and white. Please see our company logo attached, and our website is is www.corvalenpc.com

```html
<!DOCTYPE html>
<html lang="en">
<head>
<meta charset="utf-8">
<title>Corvalen Technologies Support Card</title>
<link rel="stylesheet" href="https://fonts.googleapis.com/css2?family=Outfit:wght@500;600&family=Arimo:wght@400&family=Cormorant+Garamond:wght@600&display=swap">
<style>
  :root {
    --band: #c8cfe5;
    --paper: #ffffff;
    --ink: #1f1b1b;
    --charcoal: #332a2a;
    --brand-red: #c20018;
    --rule: #1c1a1a;
  }
  * { margin: 0; padding: 0; box-sizing: border-box; }
  html, body { width: 1200px; height: 1199px; overflow: hidden; background: var(--paper); }
  .card { position: relative; width: 1200px; height: 1199px; background: var(--paper); }
  .hero-band { position: absolute; left: 0; top: 0; width: 1200px; height: 599px; background: var(--band); }
  .headline {
    position: absolute; left: 61px; top: 11px; white-space: nowrap;
    font-family: "Outfit", sans-serif; font-weight: 600; font-size: 64px; line-height: 1.26;
    color: var(--charcoal); letter-spacing: -0.5px;
  }
  .brand-dot { position: absolute; border-radius: 50%; background: var(--brand-red); }
  .brand-dot.large { left: 118px; top: 200px; width: 200px; height: 200px; }
  .brand-dot.small { left: 62px; top: 668px; width: 80px; height: 80px; }
  .brand-name {
    position: absolute; font-family: "Arimo", sans-serif; font-weight: 400;
    color: var(--charcoal); white-space: nowrap;
  }
  .brand-name.large { left: 415px; top: 190px; font-size: 121px; line-height: 108px; letter-spacing: -1px; }
  .brand-name.small { left: 180px; top: 668px; font-size: 45px; line-height: 40px; }
  .values {
    position: absolute; left: 58px; top: 491px; white-space: nowrap;
    font-family: "Outfit", sans-serif; font-weight: 600; font-size: 34px; line-height: 38px;
    color: var(--charcoal);
  }
  .divider { position: absolute; left: 0; top: 792px; width: 1200px; height: 6px; background: var(--rule); }
  .contact-list {
    position: absolute; left: 52px; top: 877px;
    font-family: "Outfit", sans-serif; font-weight: 600; font-size: 50px; color: var(--ink);
  }
  .contact-row { display: flex; height: 65.5px; line-height: 65.5px; white-space: nowrap; }
  .contact-label { width: 364px; }
  .qr-label {
    position: absolute; left: 963px; top: 966px;
    font-family: "Cormorant Garamond", serif; font-weight: 600; font-size: 60px; line-height: 1;
    color: var(--charcoal);
  }
</style>
</head>
<body>
<main class="card">
  <section class="hero-band">
    <h1 class="headline">Experience is Everything</h1>
    <div class="brand-dot large"></div>
    <p class="brand-name large">Corvalen<br>Technologies</p>
    <p class="values">Obsessed with Impossible<br>Consistency Over Time Equals Trust</p>
  </section>

  <div class="brand-dot small"></div>
  <p class="brand-name small">Corvalen<br>Technologies</p>

  <div class="divider"></div>

  <dl class="contact-list">
    <div class="contact-row"><dt class="contact-label">Name</dt><dd>:</dd></div>
    <div class="contact-row"><dt class="contact-label">Email</dt><dd>:</dd></div>
    <div class="contact-row"><dt class="contact-label">Website</dt><dd>:</dd></div>
    <div class="contact-row"><dt class="contact-label">Phone Number</dt><dd>:</dd></div>
  </dl>

  <p class="qr-label" aria-label="QR code: scan for support">QR</p>
</main>
</body>
</html>
```